Bath Salt - Sachet Packet (5 Scents) Packaging Design

We sell products to professional salons in the USA. This product is used as the first step when treating clients to a pedicure spa. This product is called SALT SOAK (or Bath Salts). The salt is added to the water to cleanse the skin, create a pleasant fragrance, and change the color of the water.

This product has 5 different variations, based on the scent of the salt soak. The available scents are:
LAVENDER, MANDARIN, CUCUMBER-MELON, JASMINE, MINT.

We would like to see package designs for all 5 scents. The theme should be consistent across the different variations of scents. The design should focus on bright, attractive, floral colors/themes. The design should fully express the color and imagery that are associated with each scent. (Lavender scent should include purple colors, lavender flower, etc.). See example images for reference of popular designs/brands.

Ideal designs will incorporate a luxurious and premium aesthetic that combines elegant imagery, colors, and premium finishes. See example images for reference of popular designs/brands.

Each packet is individually sealed. See dimension artwork file for reference of the sachet packet size and layout.

See the attached document guidelines for more information about product name, key text, and brand logo.

Target Market(s)

Beauty & Nail Salons

Industry/Entity Type

Beauty

Font styles to use
Sans Serif
Script

Requirements
Must have
• Bright imagery and colors that relate to the target fragrance
Nice to have
• Premium and luxurious finishes (shiny accent, etc.)

```html
<!DOCTYPE html>
<html lang="en">
<head>
<meta charset="utf-8">
<title>Velora Sea Salt Soak – Sachet Range</title>
<link href="https://fonts.googleapis.com/css2?family=Questrial&family=Great+Vibes&display=swap" rel="stylesheet">
<style>
  :root {
    --bg: #4d4f52;
    --ink: #4a4a4c;
    --ink-soft: #6a6a6c;
    --gold-hi: #fff3b8;
    --gold-mid: #e2c060;
    --gold-lo: #b08a2c;
    --mandarin: #f4ba8e;
    --mandarin-light: #fce2c9;
    --mint: #aadcd6;
    --mint-light: #dff0ec;
    --jasmine: #dcd8c5;
    --jasmine-light: #f6f4ec;
    --cucumber: #b3dca3;
    --cucumber-light: #d8edcf;
    --lavender: #aeaad7;
    --lavender-light: #dcdcf0;
  }
  * { margin: 0; padding: 0; box-sizing: border-box; }
  html, body { width: 1200px; height: 900px; overflow: hidden; }
  body {
    background: var(--bg);
    font-family: "Questrial", sans-serif;
    color: var(--ink);
    position: relative;
  }
  .range {
    position: absolute;
    left: 46px; top: 129px;
    display: grid;
    grid-template-columns: repeat(5, 181px);
    grid-template-rows: 292px 293px;
    column-gap: 51px;
    row-gap: 58px;
  }
  .sachet { position: relative; width: 181px; height: 100%; text-align: center; }
  .sachet__tab {
    position: absolute; left: 2px; right: 2px; top: 0; height: 48px;
    background: var(--tone); border-radius: 6px 6px 0 0;
  }
  .sachet__body {
    position: absolute; left: 0; right: 0; top: 45px; bottom: 0;
    background: var(--tone); border-radius: 6px;
  }
  .sachet--back .sachet__body { background: var(--tone-light); }
  .sachet > .layer { position: absolute; left: 0; right: 0; }

  .mandarin { --tone: var(--mandarin); --tone-light: var(--mandarin-light); }
  .mint { --tone: var(--mint); --tone-light: var(--mint-light); }
  .jasmine { --tone: var(--jasmine); --tone-light: var(--jasmine-light); }
  .cucumber { --tone: var(--cucumber); --tone-light: var(--cucumber-light); }
  .lavender { --tone: var(--lavender); --tone-light: var(--lavender-light); }

  .seal-label { top: 10px; font-size: 6.5px; letter-spacing: 0.9px; }
  .brand-name { font-size: 21px; letter-spacing: 0.5px; color: var(--ink); }
  .front .brand-name { top: 43px; }
  .artwork {
    position: absolute; left: 50px; width: 81px; top: 78px; height: 78px;
    border-radius: 50%;
    background: radial-gradient(circle at 40% 35%, var(--gold-hi), var(--gold-mid) 45%, var(--gold-lo) 75%, transparent 76%);
    opacity: 0.9;
  }
  .scent-name { top: 159px; font-size: 19px; letter-spacing: 2.4px; line-height: 1; }
  .scent-name--two-line { top: 150px; font-size: 16px; line-height: 1.05; }
  .product-name { top: 197px; font-size: 13px; letter-spacing: 1.4px; }
  .script-line { top: 212px; font-family: "Great Vibes", cursive; font-size: 16px; color: var(--ink); }
  .net-weight { top: 253px; font-size: 7px; letter-spacing: 0.6px; }

  .back .seal-label { top: 10px; }
  .back .product-name { top: 27px; }
  .back-artwork {
    position: absolute; left: 10px; right: 10px; top: 190px; height: 80px;
    background: radial-gradient(ellipse at 50% 50%, rgba(255,255,255,0.35), transparent 70%);
  }
  .directions { top: 64px; font-size: 6px; line-height: 1.4; padding: 0 20px; color: var(--ink-soft); }
  .directions strong { display: block; color: var(--ink); font-weight: normal; letter-spacing: 0.4px; }
  .caution {
    position: absolute; left: 16px; right: 14px; top: 100px; height: 76px;
    border: 0.8px dashed var(--ink-soft); border-radius: 2px;
    padding: 6px 5px 0; font-size: 5.4px; line-height: 1.5; color: var(--ink-soft);
  }
  .caution strong { display: block; color: var(--ink); font-weight: normal; font-size: 6px; letter-spacing: 0.4px; }
  .back .brand-name { top: 188px; }
  .distributor { top: 218px; font-size: 5.6px; line-height: 1.3; color: var(--ink); }
  .distributor strong { font-weight: normal; display: block; }
  .origin { top: 263px; font-size: 6.5px; letter-spacing: 0.8px; }
</style>
</head>
<body>
<main class="range">

  <!-- Fronts -->
  <section class="sachet front mandarin">
    <div class="sachet__tab"></div><div class="sachet__body"></div>
    <p class="layer seal-label">SEALED FRESH</p>
    <p class="layer brand-name">Velora</p>
    <div class="artwork" role="img" aria-label="Gold foil mandarin slice with line-drawn citrus and leaves"></div>
    <h2 class="layer scent-name">MANDARIN</h2>
    <p class="layer product-name">SEA SALT SOAK</p>
    <p class="layer script-line">Deluxe Pedicure</p>
    <p class="layer net-weight">Net 25g e 0.88 oz.</p>
  </section>
  <section class="sachet front mint">
    <div class="sachet__tab"></div><div class="sachet__body"></div>
    <p class="layer seal-label">SEALED FRESH</p>
    <p class="layer brand-name">Velora</p>
    <div class="artwork" role="img" aria-label="Gold foil mint leaf with line-drawn mint sprigs"></div>
    <h2 class="layer scent-name">MINT</h2>
    <p class="layer product-name">SEA SALT SOAK</p>
    <p class="layer script-line">Deluxe Pedicure</p>
    <p class="layer net-weight">Net 25g e 0.88 oz.</p>
  </section>
  <section class="sachet front jasmine">
    <div class="sachet__tab"></div><div class="sachet__body"></div>
    <p class="layer seal-label">SEALED FRESH</p>
    <p class="layer brand-name">Velora</p>
    <div class="artwork" role="img" aria-label="Gold foil jasmine blossom with line-drawn leaves"></div>
    <h2 class="layer scent-name">JASMINE</h2>
    <p class="layer product-name">SEA SALT SOAK</p>
    <p class="layer script-line">Deluxe Pedicure</p>
    <p class="layer net-weight">Net 25g e 0.88 oz.</p>
  </section>
  <section class="sachet front cucumber">
    <div class="sachet__tab"></div><div class="sachet__body"></div>
    <p class="layer seal-label">SEALED FRESH</p>
    <p class="layer brand-name">Velora</p>
    <div class="artwork" role="img" aria-label="Gold foil cucumber slice with line-drawn melon"></div>
    <h2 class="layer scent-name scent-name--two-line">CUCUMBER<br>MELON</h2>
    <p class="layer product-name">SEA SALT SOAK</p>
    <p class="layer script-line">Deluxe Pedicure</p>
    <p class="layer net-weight">Net 25g e 0.88 oz.</p>
  </section>
  <section class="sachet front lavender">
    <div class="sachet__tab"></div><div class="sachet__body"></div>
    <p class="layer seal-label">SEALED FRESH</p>
    <p class="layer brand-name">Velora</p>
    <div class="artwork" role="img" aria-label="Gold and white lavender sprigs"></div>
    <h2 class="layer scent-name">LAVENDER</h2>
    <p class="layer product-name">SEA SALT SOAK</p>
    <p class="layer script-line">Deluxe Pedicure</p>
    <p class="layer net-weight">Net 25g e 0.88 oz.</p>
  </section>

  <!-- Backs -->
  <section class="sachet sachet--back back mandarin">
    <div class="sachet__tab"></div><div class="sachet__body"></div>
    <div class="back-artwork" role="img" aria-label="Faint line-drawn citrus slices"></div>
    <p class="layer seal-label">SINGLE-USE</p>
    <p class="layer product-name">SEA SALT SOAK</p>
    <p class="layer directions"><strong>DIRECTIONS:</strong>Add desired amount to warm water, soak feet, and then rinse.</p>
    <p class="caution"><strong>CAUTION:</strong>For external use only. Avoid use when skin is damaged or near any open cuts, wounds, or irritations. If signs of irritation occur, stop use immediately and consult a doctor. Keep away from direct sunlight. Store at room temperature and use immediately after opening. Keep out of reach of children.</p>
    <p class="layer brand-name">Velora</p>
    <p class="layer distributor"><strong>Distributed by:</strong>Blue Harbor Supply, Inc.<br>Fairview, IN 46000<br>www.blueharborsupply.com</p>
    <p class="layer origin">Made in Korea</p>
  </section>
  <section class="sachet sachet--back back mint">
    <div class="sachet__tab"></div><div class="sachet__body"></div>
    <div class="back-artwork" role="img" aria-label="Faint line-drawn mint leaves"></div>
    <p class="layer seal-label">SINGLE-USE</p>
    <p class="layer product-name">SEA SALT SOAK</p>
    <p class="layer directions"><strong>DIRECTIONS:</strong>Add desired amount to warm water, soak feet, and then rinse.</p>
    <p class="caution"><strong>CAUTION:</strong>For external use only. Avoid use when skin is damaged or near any open cuts, wounds, or irritations. If signs of irritation occur, stop use immediately and consult a doctor. Keep away from direct sunlight. Store at room temperature and use immediately after opening. Keep out of reach of children.</p>
    <p class="layer brand-name">Velora</p>
    <p class="layer distributor"><strong>Distributed by:</strong>Blue Harbor Supply, Inc.<br>Fairview, IN 46000<br>www.blueharborsupply.com</p>
    <p class="layer origin">Made in Korea</p>
  </section>
  <section class="sachet sachet--back back jasmine">
    <div class="sachet__tab"></div><div class="sachet__body"></div>
    <div class="back-artwork" role="img" aria-label="Faint line-drawn jasmine flowers"></div>
    <p class="layer seal-label">SINGLE-USE</p>
    <p class="layer product-name">SEA SALT SOAK</p>
    <p class="layer directions"><strong>DIRECTIONS:</strong>Add desired amount to warm water, soak feet, and then rinse.</p>
    <p class="caution"><strong>CAUTION:</strong>For external use only. Avoid use when skin is damaged or near any open cuts, wounds, or irritations. If signs of irritation occur, stop use immediately and consult a doctor. Keep away from direct sunlight. Store at room temperature and use immediately after opening. Keep out of reach of children.</p>
    <p class="layer brand-name">Velora</p>
    <p class="layer distributor"><strong>Distributed by:</strong>Blue Harbor Supply, Inc.<br>Fairview, IN 46000<br>www.blueharborsupply.com</p>
    <p class="layer origin">Made in Korea</p>
  </section>
  <section class="sachet sachet--back back cucumber">
    <div class="sachet__tab"></div><div class="sachet__body"></div>
    <div class="back-artwork" role="img" aria-label="Faint line-drawn cucumber and melon"></div>
    <p class="layer seal-label">SINGLE-USE</p>
    <p class="layer product-name">SEA SALT SOAK</p>
    <p class="layer directions"><strong>DIRECTIONS:</strong>Add desired amount to warm water, soak feet, and then rinse.</p>
    <p class="caution"><strong>CAUTION:</strong>For external use only. Avoid use when skin is damaged or near any open cuts, wounds, or irritations. If signs of irritation occur, stop use immediately and consult a doctor. Keep away from direct sunlight. Store at room temperature and use immediately after opening. Keep out of reach of children.</p>
    <p class="layer brand-name">Velora</p>
    <p class="layer distributor"><strong>Distributed by:</strong>Blue Harbor Supply, Inc.<br>Fairview, IN 46000<br>www.blueharborsupply.com</p>
    <p class="layer origin">Made in Korea</p>
  </section>
  <section class="sachet sachet--back back lavender">
    <div class="sachet__tab"></div><div class="sachet__body"></div>
    <div class="back-artwork" role="img" aria-label="Faint line-drawn lavender sprigs"></div>
    <p class="layer seal-label">SINGLE-USE</p>
    <p class="layer product-name">SEA SALT SOAK</p>
    <p class="layer directions"><strong>DIRECTIONS:</strong>Add desired amount to warm water, soak feet, and then rinse.</p>
    <p class="caution"><strong>CAUTION:</strong>For external use only. Avoid use when skin is damaged or near any open cuts, wounds, or irritations. If signs of irritation occur, stop use immediately and consult a doctor. Keep away from direct sunlight. Store at room temperature and use immediately after opening. Keep out of reach of children.</p>
    <p class="layer brand-name">Velora</p>
    <p class="layer distributor"><strong>Distributed by:</strong>Blue Harbor Supply, Inc.<br>Fairview, IN 46000<br>www.blueharborsupply.com</p>
    <p class="layer origin">Made in Korea</p>
  </section>

</main>
</body>
</html>
```